Dovantix - "Where Pest Control is Free for Life..." Please see pitch deck...

Project goal, that this is a reusable template, not a one-off card
Brand and design direction, follow the logo, use the brand palette (with a color swatch table), typography and layout guidance
The John Doe placeholder content as a clean field-by-field table (name, title, company, address, office, cell, fax, email, dovantix.com)
Print specs, 3.5 × 2 in trim, 0.125 in bleed, 300 DPI, CMYK, crop marks
Deliverables, layered editable PSD (your primary ask) plus vector .AI/.EPS and a press-ready PDF/X-1a, with fonts packaged
What you'll provide (logo, colors, fonts)
Process and sign-off, concept first, then full file package on approval.
Populate every field with this John Doe placeholder data so we can see the layout fully built out. We will replace it per person.
Name John Doe
Title Title / Position
Company Dovantix
Address 123 Main Street, Suite 100, Tallahassee, FL 32301
Office (850) 555-0100
Cell (850) 555-0123
Fax (850) 555-0199
Email johndoe@dovantix.com
Website dovantix.com

We need the working, editable source files so we can update them ourselves, plus a ready-to-print export:
1. Photoshop (.PSD) — fully layered and editable, with each contact field on its own labeled text layer. This is the primary requested format.
2. Vector source — the press-standard editable format, Adobe Illustrator (.AI) and/or .EPS, since vector is preferred for crisp text and logos at print.
3. Print-ready PDF — press-quality (PDF/X-1a), CMYK, with bleed and crop marks, both sides.
4. Packaged fonts and links — include or list all fonts used, and package any linked assets so the files open correctly on our end.

Why both PSD and vector
The PSD covers our request directly and is easy for us to edit. Vector (.AI/.EPS) is what most commercial printers actually prefer for type and logos because it stays razor-sharp at any size. Providing both keeps us flexible no matter which printer we use. Have fun and keep it modern and cool the designer of the logo did a great job, see what you can do.

```html
<!DOCTYPE html>
<html lang="en">
<head>
<meta charset="utf-8">
<title>Dovantix Business Card</title>
<link rel="stylesheet" href="https://fonts.googleapis.com/css2?family=Montserrat:wght@400;500;700;800&display=swap">
<style>
  :root {
    --stage: #2b2b2d;
    --card-navy: #0e1327;
    --card-navy-light: #1a2140;
    --brand-teal: #1fb3c6;
    --text-white: #ffffff;
    --text-soft: #e6e9f0;
  }
  * { margin: 0; padding: 0; box-sizing: border-box; }
  html, body { width: 1200px; height: 875px; overflow: hidden; }
  body {
    background: var(--stage);
    font-family: "Montserrat", Arial, sans-serif;
    position: relative;
  }
  .card {
    position: absolute;
    width: 700px;
    height: 400px;
    border-radius: 26px;
    background: var(--card-navy);
    overflow: hidden;
  }
  .card--front {
    left: 250px; top: 25px;
    background: linear-gradient(120deg, var(--card-navy-light) 0%, var(--card-navy) 45%);
  }
  .card--back { left: 250px; top: 450px; }

  .front-wordmark {
    position: absolute;
    inset: 0;
    display: flex; align-items: center; justify-content: center; gap: 18px;
  }
  .front-wordmark__name {
    font-weight: 800;
    font-size: 104px;
    letter-spacing: -2px;
    color: var(--text-white);
    line-height: 1;
    white-space: nowrap;
  }
  .front-wordmark__mark {
    flex: none;
    width: 34px; height: 34px;
    background: var(--brand-teal);
    margin-top: 38px;
  }

  .back-brand {
    position: absolute;
    left: 44px; top: 150px;
    width: auto;
  }
  .back-brand__name {
    display: flex; align-items: center; gap: 8px;
    font-weight: 800; font-size: 56px; letter-spacing: -1px;
    color: var(--text-white); line-height: 1;
    white-space: nowrap;
  }
  .back-brand__mark {
    flex: none;
    width: 16px; height: 16px;
    background: var(--brand-teal);
    margin-top: 20px;
  }
  .back-brand__tagline {
    margin-top: 10px;
    font-weight: 700; font-size: 13px; letter-spacing: 1.1px;
    color: var(--text-white);
    white-space: nowrap;
  }
  .back-brand__subline {
    margin-top: 3px;
    font-weight: 500; font-size: 12.5px;
    color: var(--brand-teal);
    white-space: nowrap;
  }

  .divider {
    position: absolute;
    left: 372px; top: 70px;
    width: 2px; height: 260px;
    background: var(--brand-teal);
  }

  .contact {
    position: absolute;
    left: 398px; top: 64px;
    color: var(--text-soft);
  }
  .contact__name {
    font-weight: 700; font-size: 30px; color: var(--brand-teal); line-height: 1.1;
  }
  .contact__title { font-size: 14px; margin-top: 3px; }
  .contact__address { font-size: 14px; line-height: 1.45; margin-top: 16px; }
  .contact__list { list-style: none; margin-top: 16px; }
  .contact__item {
    display: flex; align-items: center; gap: 10px;
    font-size: 14px; line-height: 1.55;
  }
  .contact__icon { width: 14px; height: 14px; flex: none; fill: var(--brand-teal); }
</style>
</head>
<body>

  <section class="card card--front" aria-label="Card front">
    <div class="front-wordmark">
      <span class="front-wordmark__name">Dovantix</span>
      <span class="front-wordmark__mark"></span>
    </div>
  </section>

  <section class="card card--back" aria-label="Card back">
    <div class="back-brand">
      <div class="back-brand__name">Dovantix<span class="back-brand__mark"></span></div>
      <p class="back-brand__tagline">WE PROTECT WHERE YOU LIVE</p>
      <p class="back-brand__subline">Pest control free for life</p>
    </div>

    <div class="divider"></div>

    <div class="contact">
      <p class="contact__name">John Doe</p>
      <p class="contact__title">Title / Position</p>
      <p class="contact__address">123 Main Street, Suite 100,<br>Tallahassee, FL 32301</p>
      <ul class="contact__list">
        <li class="contact__item">
          <svg class="contact__icon" viewBox="0 0 16 16" aria-hidden="true"><path d="M1 6c0-2 3-4 7-4s7 2 7 4v1h-4V5.5H5V7H1zM3 8h10l1 6H2z"/></svg>
          (850) 555-0100
        </li>
        <li class="contact__item">
          <svg class="contact__icon" viewBox="0 0 16 16" aria-hidden="true"><path d="M4 1h8v14H4zM5.5 2.5v9h5v-9zM7 12.5h2v1.2H7z" fill-rule="evenodd"/></svg>
          (850) 555-0123
        </li>
        <li class="contact__item">
          <svg class="contact__icon" viewBox="0 0 16 16" aria-hidden="true"><path d="M4 1h8v4H4zM1 6h14v6h-3v3H4v-3H1zM5.5 10v3.5h5V10z" fill-rule="evenodd"/></svg>
          (850) 555-0199
        </li>
        <li class="contact__item">
          <svg class="contact__icon" viewBox="0 0 16 16" aria-hidden="true"><path d="M1 3h14v10H1zM2.5 4.5 8 9l5.5-4.5z" fill-rule="evenodd"/></svg>
          johndoe@dovantix.com
        </li>
        <li class="contact__item">
          <svg class="contact__icon" viewBox="0 0 16 16" aria-hidden="true"><circle cx="8" cy="8" r="7"/><path d="M1 8h14M8 1c-3 3-3 11 0 14M8 1c3 3 3 11 0 14" stroke="#0e1327" stroke-width="1.1" fill="none"/></svg>
          dovantix.com
        </li>
      </ul>
    </div>
  </section>

</body>
</html>
```